High-End Medical Center Website Design Project

This design is part of a well thought-out project by an experienced project manager / developer. The approved wireframe is attached. Creative interpretations / suggestions based on the layout encouraged.

The design is for a new state-of-the-art medical center located in Dallas, Texas. The target audience would likely be individuals (approx. 60% female /40% male) who are the healthcare decision-makers for their families. They would likely have insurance and be inclined to seek out top-quality care.

Potential clients would choose this client over others in their industry because the medical center is physician owned, meaning it is patient-focused rather than profit-focused. The facility is brand new, featuring the latest technology. (This includes an amazing waiting room featuring WiFi and docking stations.) The physicians are hand-picked by referral only.

The look of the site should be extremely clean. We are going for a well-organized, professional look with a bit of a warm glow (interpret that however you like). Use crisp corners and the colors in the logo.

Think modern, clean with some great use of color / font.

We can get lovely photography of the medical center once construction is complete. Feel free to use an "example image" behind the Featured Area ("Physician Owned. Patient-Focused") if you like. We are open to ideas.

ONE CHANGE REQUESTED IN THE WIREFRAME:

Remove the "Connect" 1/4 page footer area and replace with a quick contact form. You may swap the "Locations" area with the form if desired. Put social media icons at the top left of the page in the top header area.

(Note: Please use social media icons that match the design rather than standard icons. We preferred not placing the icons at the top, but the client requested this. Let's not bring more attention to them than necessary.)
Updates

We're custom programming this site, so there's no need to base it on a template. Also, we would prefer not to use typical "seen everywhere" stock images.Thanks.

Industry/Entity Type

Construction

Requirements
Must have
• Follow the wireframe. This has been approved.
Nice to have
• Examples of what hover states, links or dropdowns might look like.

```html
<!DOCTYPE html>
<html lang="en">
<head>
<meta charset="utf-8">
<title>Crest Medical Center</title>
<link href="https://fonts.googleapis.com/css2?family=Roboto+Condensed:wght@400;700&family=Open+Sans:ital,wght@0,400;0,600;0,700;1,600;1,700&display=swap" rel="stylesheet">
<style>
:root{
  --blue:#0b5aac;
  --blue-dark:#084a8e;
  --teal:#3a9fb1;
  --ink:#222;
  --text:#555;
  --grey-icon:#4a4a4a;
  --social-grey:#9b9b9b;
  --topbar:#e2e2e2;
  --hero-bg:#f6f6f6;
  --footer-bg:#ececec;
  --line:#dcdcdc;
  --white:#fff;
}
*{margin:0;padding:0;box-sizing:border-box}
html,body{width:996px;height:1200px;overflow:hidden;background:var(--white)}
body{position:relative;font-family:'Open Sans',Arial,sans-serif;color:var(--text)}
.abs{position:absolute}
.cond{font-family:'Roboto Condensed','Arial Narrow',sans-serif}

/* top bar */
.topbar{left:0;top:0;width:996px;height:40px;background:var(--topbar)}
.social{display:flex;gap:3px}
.social span{display:block;width:28px;height:28px;background:var(--social-grey)}
.social span.on{background:var(--blue)}
.social a:hover span{background:var(--blue)}
.topbar .social{position:absolute;left:105px;top:5px}
.call{right:102px;top:7px;font-size:20px;color:var(--teal)}
.call b{font-weight:400;color:var(--blue-dark)}

/* hero */
.hero{left:0;top:40px;width:996px;height:512px;background:var(--hero-bg)}
.hero-photo{left:320px;top:100px;width:560px;height:372px;
  background:linear-gradient(100deg,#f4f6f8 0%,#dfe6ee 30%,#c9d7e6 55%,#eedcc9 75%,#9ec8d8 100%)}
.brand{left:316px;top:70px;display:flex;align-items:center;gap:12px}
.brand i{display:block;width:46px;height:46px;background:var(--blue)}
.brand span{font-family:'Roboto Condensed','Arial Narrow',sans-serif;font-weight:700;font-size:40px;color:var(--blue);letter-spacing:1px;text-transform:uppercase}
.nav{left:105px;top:148px;width:791px;height:42px;background:var(--white);border:1px solid var(--line);display:flex;box-shadow:0 4px 6px -4px rgba(0,0,0,.15)}
.nav a{font-family:'Roboto Condensed','Arial Narrow',sans-serif;font-size:20px;color:#666;text-decoration:none;line-height:40px;padding:0 27px 0 22px;border-right:1px solid #e6e6e6}
.nav a:last-child{border-right:0}
.nav a.current,.nav a:hover{color:var(--blue)}
.hero-title{left:111px;top:240px;font-size:40px;line-height:40px;font-weight:700;color:var(--blue)}
.hero-sub{left:113px;top:333px;font-size:19px;line-height:20px;color:var(--ink)}
.stars{left:119px;top:416px;display:flex;gap:7px}

/* features */
.features{left:105px;top:472px;width:791px;height:226px;background:var(--white);border:1px solid var(--line);display:flex;box-shadow:0 6px 8px -6px rgba(0,0,0,.18)}
.feature{flex:1;text-align:center;border-right:1px solid #e6e6e6;padding-top:11px}
.feature:last-child{border-right:0}
.circle-icon{width:52px;height:52px;border-radius:50%;margin:0 auto;display:flex;align-items:center;justify-content:center;background:var(--grey-icon)}
.circle-icon.blue{background:var(--blue)}
.feature h3{font-family:'Roboto Condensed','Arial Narrow',sans-serif;font-weight:400;font-size:20px;color:#444;margin-top:14px}
.feature h3.blue{color:var(--blue)}
.feature p{font-size:10.5px;line-height:17.5px;width:205px;margin:14px auto 0;color:#444}

/* intro */
.intro-photo{left:106px;top:737px;width:170px;height:168px;background:var(--white);border:1px solid #ccc;box-shadow:0 1px 4px rgba(0,0,0,.25);padding:5px}
.intro-photo div{width:100%;height:100%;background:linear-gradient(135deg,#dfe9ee 0%,#b7d5e8 40%,#2f7fc4 70%,#1e5e9e 100%)}
.intro-title{left:297px;top:741px;font-size:20px;color:var(--blue)}
.intro-text{left:298px;top:776px;width:355px;font-size:10.5px;line-height:17.5px;text-align:justify;color:#666}
.read-more{left:299px;top:878px;font-size:9px;font-weight:700;font-style:italic;color:var(--blue);text-decoration:none}
.testi-title{left:709px;top:733px;font-size:20px;font-weight:700;color:var(--blue);font-weight:400}
.testi{left:709px;top:769px;width:179px;font-size:10.5px;line-height:17.5px;text-align:justify;color:#444}
.testi svg{float:left;margin:10px 10px 4px 0}
.testi-name{left:709px;top:886px;font-size:9.5px;font-weight:600;font-style:italic;color:var(--blue)}

/* footer */
.footer{left:0;top:940px;width:996px;height:225px;background:var(--footer-bg)}
.fdiv{top:940px;width:1px;height:225px;background:#d8d8d8}
.fhead{display:flex;align-items:center;gap:8px;font-family:'Roboto Condensed','Arial Narrow',sans-serif;font-size:18px;color:var(--blue)}
.fhead .dot{width:30px;height:30px;border-radius:50%;background:var(--blue);display:flex;align-items:center;justify-content:center}
.item{display:flex;gap:13px;width:172px;height:59px;padding:10px 0 0 15px}
.item.active{background:#d6d6d6}
.date{width:36px;height:38px;background:#cfcfcf;border:1px solid #bbb;text-align:center;font-size:14px;line-height:17px;color:#333;font-weight:700}
.date small{display:block;font-size:11px;font-weight:400;border-top:1px solid #999;margin:0 3px}
.item p{font-size:11px;line-height:16px;color:#222}
.item p small{display:block;font-size:9.5px;line-height:16px;color:#222}
.item p small.gold{color:#8a7a3a}
.item p a{font-size:10.5px;color:var(--blue);text-decoration:none}
.rule{height:1px;background:var(--blue)}
.link-btn{width:18px;height:18px;background:var(--blue);display:flex;align-items:center;justify-content:center}
.field{background:var(--white);border:1px solid #ccc;font-size:9px;font-style:italic;color:#555;padding:4px 8px}
.btn{background:var(--blue);color:var(--white);font-size:10px;font-weight:700;font-style:italic;text-align:center;line-height:20px}
.btn:hover{background:var(--blue-dark)}
.footer .social span{background:#1f1f1f}
.footer .social span.on{background:var(--blue)}

.bottombar{left:0;top:1165px;width:996px;height:35px;background:var(--blue);color:var(--white);font-size:10.5px;line-height:35px}
.bottombar .copy{position:absolute;left:105px}
.bottombar .links{position:absolute;right:101px}
.bottombar .links a{color:var(--white);text-decoration:none}
.bottombar .links a.muted{color:#0d3f7a}
</style>
</head>
<body>

<header class="abs topbar">
  <nav class="social" aria-label="Social links">
    <a href="#"><span class="on"></span></a><a href="#"><span></span></a><a href="#"><span></span></a><a href="#"><span></span></a><a href="#"><span></span></a>
  </nav>
  <div class="abs call cond">Call Now : <b>555-014-2290</b></div>
</header>

<section class="abs hero"></section>
<div class="abs hero-photo" role="img" aria-label="Photo of a physician gently examining a patient while a nurse assists"></div>
<div class="abs brand"><i></i><span>Crest Medical Center</span></div>

<nav class="abs nav">
  <a href="#" class="current">Why Crest</a>
  <a href="#">Phycisians</a>
  <a href="#">Specialities</a>
  <a href="#">Info</a>
  <a href="#">Locations</a>
  <a href="#">Contact Us</a>
</nav>

<h1 class="abs hero-title cond">Lorem ipsum<br>dolor</h1>
<p class="abs hero-sub cond">Consectetur adipiscing elit.<br>Aliquam malesuada augue<br>eget mattis ultricies.</p>
<div class="abs stars">
  <svg width="17" height="17" viewBox="0 0 24 24"><path d="M12 1l3.3 7 7.7.9-5.7 5.2 1.6 7.6L12 17.9 5.1 21.7l1.6-7.6L1 8.9 8.7 8z" fill="#0b5aac"/></svg>
  <svg width="17" height="17" viewBox="0 0 24 24"><path d="M12 1l3.3 7 7.7.9-5.7 5.2 1.6 7.6L12 17.9 5.1 21.7l1.6-7.6L1 8.9 8.7 8z" fill="#ccc"/></svg>
  <svg width="17" height="17" viewBox="0 0 24 24"><path d="M12 1l3.3 7 7.7.9-5.7 5.2 1.6 7.6L12 17.9 5.1 21.7l1.6-7.6L1 8.9 8.7 8z" fill="#ccc"/></svg>
  <svg width="17" height="17" viewBox="0 0 24 24"><path d="M12 1l3.3 7 7.7.9-5.7 5.2 1.6 7.6L12 17.9 5.1 21.7l1.6-7.6L1 8.9 8.7 8z" fill="#ccc"/></svg>
  <svg width="17" height="17" viewBox="0 0 24 24"><path d="M12 1l3.3 7 7.7.9-5.7 5.2 1.6 7.6L12 17.9 5.1 21.7l1.6-7.6L1 8.9 8.7 8z" fill="#ccc"/></svg>
</div>

<section class="abs features">
  <div class="feature">
    <div class="circle-icon blue"><svg width="28" height="28" viewBox="0 0 28 28" fill="none" stroke="#fff" stroke-width="2.2"><path d="M6 9c0-4 5-5 8-3 4 2 9 1 9 6 0 6-8 6-10 10"/><circle cx="6" cy="13" r="2"/><circle cx="12" cy="15" r="2"/></svg></div>
    <h3 class="blue">Technology</h3>
    <p>Lorem ipsum dolor sit amet, consectetur adipiscing elit. Aliquam malesuada augue eget mattis ultricies. Maecenas felis sem, pretium quis venenatis quis, sodales nec dolor. Sed eu facilisis</p>
  </div>
  <div class="feature">
    <div class="circle-icon"><svg width="28" height="28" viewBox="0 0 28 28" fill="none" stroke="#fff" stroke-width="2"><rect x="5" y="7" width="15" height="15"/><path d="M9 14l3 3 11-12"/></svg></div>
    <h3>Quality of care</h3>
    <p>Lorem ipsum dolor sit amet, consectetur adipiscing elit. Aliquam malesuada augue eget mattis ultricies. Maecenas felis sem, pretium quis venenatis quis, sodales nec dolor. Sed eu facilisis metu</p>
  </div>
  <div class="feature">
    <div class="circle-icon"><svg width="28" height="28" viewBox="0 0 28 28" fill="none" stroke="#fff" stroke-width="2.2"><path d="M6 9c0-4 5-5 8-3 4 2 9 1 9 6 0 6-8 6-10 10"/><circle cx="6" cy="13" r="2"/><circle cx="12" cy="15" r="2"/></svg></div>
    <h3>Patient Exprience</h3>
    <p>Lorem ipsum dolor sit amet, consectetur adipiscing elit. Aliquam malesuada augue eget mattis ultricies. Maecenas felis sem, pretium quis venenatis quis, sodales nec dolor. Sed eu facilisis metu</p>
  </div>
</section>

<div class="abs intro-photo"><div role="img" aria-label="Photo of a smiling nurse in blue scrubs holding a tablet"></div></div>
<h2 class="abs intro-title cond" style="font-weight:400">Lorem ipsum dolor sit</h2>
<p class="abs intro-text">Lorem ipsum dolor sit amet, consectetur adipiscing elit. Aliquam malesuada augue eget mattis ultricies. Maecenas felis sem, pretium quis venenatis quis, sodales nec dolor. Sed eu facilisis metus, non consectetur arcu. Nam in fermentum arcu, iaculis condimentum orci. Suspendisse consequat, diam vel lobortis pulvinar, odio lacus dapibus erat, sed sollicitudin</p>
<a class="abs read-more" href="#">Read more....</a>

<h2 class="abs testi-title cond">Our Testimonials</h2>
<p class="abs testi"><svg width="24" height="20" viewBox="0 0 24 20"><path d="M2 2h13v8H7l-4 3v-3H2z" fill="#0b5aac"/><path d="M10 12h8l3 3v-3h1V5h-4v7z" fill="#0b5aac"/></svg>Lorem ipsum dolor sit amet, consectetur adipiscing elit. Integer molestie quam a Lorem ipsum dolor sit amet, consectetur adipiscing elit. Integer molestie quam a magna iaculis</p>
<div class="abs testi-name">Customer Name</div>

<footer class="abs footer"></footer>
<div class="abs fdiv" style="left:306px"></div>
<div class="abs fdiv" style="left:523px"></div>
<div class="abs fdiv" style="left:721px"></div>

<!-- recent news -->
<div class="abs fhead" style="left:104px;top:963px"><span class="dot"><svg width="14" height="12"><rect x="1" y="1" width="12" height="10" fill="none" stroke="#fff" stroke-width="1.5"/><path d="M4 4h6M4 7h6" stroke="#fff"/></svg></span>Recent News</div>
<div class="abs item active" style="left:104px;top:1002px"><div class="date">06<small>APR</small></div><p>Lorem ipsum<small class="gold">Lorem ipsum dolor,</small><small>0 comments</small></p></div>
<div class="abs item" style="left:104px;top:1066px"><div class="date">06<small>APR</small></div><p>Lorem ipsum<small>Lorem ipsum dolor</small><small>0 comments</small></p></div>
<div class="abs rule" style="left:104px;top:1139px;width:158px"></div>
<div class="abs link-btn" style="left:258px;top:1122px"><svg width="10" height="10"><path d="M2 8l6-6M5 2h3v3" stroke="#fff" fill="none" stroke-width="1.5"/></svg></div>

<!-- recent blog -->
<div class="abs fhead" style="left:333px;top:963px"><span class="dot"><svg width="16" height="13"><path d="M1 1h10v6H5l-3 3V7H1z" fill="#fff"/><path d="M8 9h4l3 3V4h-3v5z" fill="#fff"/></svg></span>Recent Blog</div>
<div class="abs item" style="left:318px;top:1002px;width:190px"><div class="date">06<small>APR</small></div><p><small>Lorem ipsum dolor sit<br>amet lorem ipsum dolor</small><a href="#">Read more</a></p></div>
<div class="abs item" style="left:318px;top:1066px;width:190px"><div class="date">06<small>APR</small></div><p><small>Lorem ipsum dolor sit<br>amet lorem ipsum dolor</small><a href="#">Read more</a></p></div>
<div class="abs rule" style="left:333px;top:1139px;width:140px"></div>
<div class="abs link-btn" style="left:473px;top:1122px"><svg width="10" height="10"><path d="M2 8l6-6M5 2h3v3" stroke="#fff" fill="none" stroke-width="1.5"/></svg></div>

<!-- connect -->
<div class="abs fhead" style="left:541px;top:963px"><span class="dot"><svg width="16" height="13"><path d="M1 1h10v6H5l-3 3V7H1z" fill="#fff"/><path d="M8 9h4l3 3V4h-3v5z" fill="#fff"/></svg></span>Connect</div>
<nav class="abs social" style="left:541px;top:1013px" aria-label="Social links"><a href="#"><span class="on"></span></a><a href="#"><span></span></a><a href="#"><span></span></a><a href="#"><span></span></a><a href="#"><span></span></a></nav>
<div class="abs fhead" style="left:541px;top:1075px"><span class="dot"><svg width="16" height="13"><path d="M1 1h10v6H5l-3 3V7H1z" fill="#fff"/><path d="M8 9h4l3 3V4h-3v5z" fill="#fff"/></svg></span>News Latter</div>
<div class="abs field" style="left:544px;top:1121px;width:112px;height:20px;padding-top:3px">Your Email</div>
<div class="abs btn" style="left:654px;top:1121px;width:28px;height:20px;font-style:normal;font-size:9px">GO</div>

<!-- contact -->
<div class="abs fhead" style="left:740px;top:963px"><span class="dot"><svg width="16" height="13"><path d="M1 1h10v6H5l-3 3V7H1z" fill="#fff"/><path d="M8 9h4l3 3V4h-3v5z" fill="#fff"/></svg></span>Conatct Us</div>
<div class="abs field" style="left:744px;top:1002px;width:151px;height:22px">Name</div>
<div class="abs field" style="left:744px;top:1031px;width:151px;height:22px">Email</div>
<div class="abs field" style="left:744px;top:1060px;width:151px;height:46px">Message</div>
<div class="abs btn" style="left:745px;top:1119px;width:63px;height:21px">Submit</div>

<div class="abs bottombar">
  <span class="copy">Copyright© 2013 Crest medical center</span>
  <span class="links"><a href="#">Site map</a> &nbsp;/&nbsp; <a href="#" class="muted">Privacy policy</a></span>
</div>

</body>
</html>
```